Redesign of business card for Birchline Mechanical

We are looking for a new design for our business cards for Birchline Mechanical. We are a plumbing & HVAC construction company, operating on the West Coast of Canada and USA. Logo attached.
Industry/Entity Type
Construction - Plumbing & HVAC
Contact Information for Business Card
Name, address, phone numbers, email, website address
Look and feel
Each slider illustrates characteristics of the customer's brand and the style your logo design should communicate.

```html
<!DOCTYPE html>
<html lang="en">
<head>
<meta charset="utf-8">
<title>Birchline Mechanical – Business Cards</title>
<link rel="stylesheet" href="https://fonts.googleapis.com/css2?family=Raleway:wght@500;600;700&display=swap">
<style>
  :root {
    --backdrop: #2a2a2b;
    --card-dark: #303642;
    --card-dark-tone: #3a4150;
    --card-light: #ffffff;
    --ink: #2f3541;
    --ink-soft: #3d4350;
    --on-dark: #ffffff;
  }
  * { box-sizing: border-box; margin: 0; padding: 0; }
  html, body {
    width: 1200px; height: 900px; overflow: hidden;
    background: var(--backdrop);
    font-family: "Raleway", Arial, sans-serif;
  }
  .canvas { position: relative; width: 1200px; height: 900px; }
  .card {
    position: absolute; width: 513px; height: 295px;
    border-radius: 26px; overflow: hidden;
  }
  .card--dark { background: var(--card-dark); }
  .card--light { background: var(--card-light); color: var(--ink); }
  .pos-tl { left: 73px; top: 138px; }
  .pos-bl { left: 73px; top: 465px; }
  .pos-tr { left: 616px; top: 138px; }
  .pos-br { left: 616px; top: 465px; }

  .pattern-fill {
    position: absolute; inset: 0;
    background: linear-gradient(135deg, var(--card-dark-tone) 0%, var(--card-dark) 100%);
  }

  .wordmark {
    position: absolute; display: flex; align-items: center; gap: 8px;
    font-weight: 700; font-size: 15px; line-height: 1.15;
    letter-spacing: 0.02em; text-transform: uppercase;
  }
  .wordmark__square { width: 14px; height: 14px; flex: none; }
  .card--dark .wordmark { right: 40px; bottom: 38px; color: var(--on-dark); }
  .card--dark .wordmark__square { background: var(--on-dark); }
  .card--light .wordmark { right: 40px; top: 48px; color: var(--ink); }
  .card--light .wordmark__square { background: var(--ink); }

  .person { position: absolute; left: 42px; }
  .person__name { font-size: 20px; font-weight: 600; color: var(--ink-soft); }
  .person__role { font-size: 15px; font-weight: 600; color: var(--ink-soft); margin-top: 3px; }
  .person__rule { width: 22px; height: 3px; background: var(--ink); margin-top: 9px; }
  .pos-tr .person { top: 48px; }
  .pos-br .person { top: 150px; }

  .contacts { position: absolute; left: 42px; list-style: none; }
  .pos-tr .contacts { top: 219px; }
  .pos-br .contacts { top: 228px; }
  .contacts li {
    display: flex; align-items: center; gap: 10px;
    font-size: 15px; font-weight: 600; color: var(--ink-soft);
    height: 19px;
  }
  .contacts svg { width: 12px; height: 12px; flex: none; }
</style>
</head>
<body>
<main class="canvas">

  <!-- Back, patterned -->
  <section class="card card--dark pos-tl">
    <div class="pattern-fill" role="img" aria-label="Faint repeating brand pattern across the card back"></div>
    <div class="wordmark"><span class="wordmark__square"></span><span>Birchline<br>Mechanical</span></div>
  </section>

  <!-- Front, name at top -->
  <section class="card card--light pos-tr">
    <div class="person">
      <p class="person__name">Daniel Harwood</p>
      <p class="person__role">managing director</p>
    </div>
    <div class="wordmark"><span class="wordmark__square"></span><span>Birchline<br>Mechanical</span></div>
    <ul class="contacts">
      <li>
        <svg viewBox="0 0 12 12" aria-hidden="true"><rect x="0.6" y="0.6" width="10.8" height="10.8" rx="2.5" fill="none" stroke="currentColor" stroke-width="1.2"/><path d="M3.3 4.4c0-1 1-1.4 2.7-1.4s2.7.4 2.7 1.4l-1 .4-.5-.8H4.8l-.5.8zM4 6h4l.8 2.6H3.2z" fill="currentColor"/></svg>
        <span>555 5555 5555</span>
      </li>
      <li>
        <svg viewBox="0 0 12 12" aria-hidden="true"><rect x="0.6" y="0.6" width="10.8" height="10.8" rx="2.5" fill="currentColor"/><rect x="2.6" y="3.6" width="6.8" height="4.8" fill="#fff"/><path d="M2.6 3.6 6 6.3l3.4-2.7" fill="none" stroke="currentColor" stroke-width="0.9"/></svg>
        <span>d.harwood@birchlinemech.com</span>
      </li>
      <li>
        <svg viewBox="0 0 12 12" aria-hidden="true"><rect x="0.6" y="0.6" width="10.8" height="10.8" rx="2.5" fill="none" stroke="currentColor" stroke-width="1.2"/><circle cx="6" cy="6" r="3" fill="none" stroke="currentColor" stroke-width="0.9"/><path d="M3 6h6M6 3c-1.3 1.6-1.3 4.4 0 6M6 3c1.3 1.6 1.3 4.4 0 6" fill="none" stroke="currentColor" stroke-width="0.8"/></svg>
        <span>www.birchlinemech.com</span>
      </li>
    </ul>
  </section>

  <!-- Back, plain -->
  <section class="card card--dark pos-bl">
    <div class="wordmark"><span class="wordmark__square"></span><span>Birchline<br>Mechanical</span></div>
  </section>

  <!-- Front, name lower -->
  <section class="card card--light pos-br">
    <div class="wordmark"><span class="wordmark__square"></span><span>Birchline<br>Mechanical</span></div>
    <div class="person">
      <p class="person__name">Daniel Harwood</p>
      <p class="person__role">managing director</p>
      <div class="person__rule"></div>
    </div>
    <ul class="contacts">
      <li>
        <svg viewBox="0 0 12 12" aria-hidden="true"><rect x="0.6" y="0.6" width="10.8" height="10.8" rx="2.5" fill="none" stroke="currentColor" stroke-width="1.2"/><path d="M3.3 4.4c0-1 1-1.4 2.7-1.4s2.7.4 2.7 1.4l-1 .4-.5-.8H4.8l-.5.8zM4 6h4l.8 2.6H3.2z" fill="currentColor"/></svg>
        <span>555 5555 5555</span>
      </li>
      <li>
        <svg viewBox="0 0 12 12" aria-hidden="true"><rect x="0.6" y="0.6" width="10.8" height="10.8" rx="2.5" fill="currentColor"/><rect x="2.6" y="3.6" width="6.8" height="4.8" fill="#fff"/><path d="M2.6 3.6 6 6.3l3.4-2.7" fill="none" stroke="currentColor" stroke-width="0.9"/></svg>
        <span>d.harwood@birchlinemech.com</span>
      </li>
      <li>
        <svg viewBox="0 0 12 12" aria-hidden="true"><rect x="0.6" y="0.6" width="10.8" height="10.8" rx="2.5" fill="none" stroke="currentColor" stroke-width="1.2"/><circle cx="6" cy="6" r="3" fill="none" stroke="currentColor" stroke-width="0.9"/><path d="M3 6h6M6 3c-1.3 1.6-1.3 4.4 0 6M6 3c1.3 1.6 1.3 4.4 0 6" fill="none" stroke="currentColor" stroke-width="0.8"/></svg>
        <span>www.birchlinemech.com</span>
      </li>
    </ul>
  </section>

</main>
</body>
</html>
```